Couples Workshop Flyer

I need a flyer to promote a one-day workshop for couples.

I am a therapist and life-coach and the session is called: "Lantern Bridge Days, and bring out the best in each other' - so Lantern Bridge Days is the bold name for the seminar but the point of the whole workshop is in the tagline, 'and bring out the best in each other'.

The final design should compel couples to take the risk to leave their comfort zones and attend a one-day workshop on a weekend .

Target Market(s)

Couples who are interested in self-improvement and identify with change and growth.
Somehow the flyer will match their aspirations!

Requirements
Should not have
• Not too many love hearts! :)
Not too gushy - a hint of romance!

```html
<!DOCTYPE html>
<html lang="en">
<head>
<meta charset="utf-8">
<title>Lantern Bridge Days – Couples Workshop</title>
<link href="https://fonts.googleapis.com/css2?family=Courgette&family=Delius&family=Dancing+Script:wght@600&display=swap" rel="stylesheet">
<style>
  :root {
    --ink: #1d1d1d;
    --paper: #ffffff;
    --sky-mist: #e9ecef;
    --hill-blue: #a9b2bd;
    --sea-grey: #8d97a3;
    --sand-gold: #b59a66;
    --wet-sand: #c5cdd4;
    --card-veil: rgba(255,255,255,0.84);
    --photo-tone: #9aa29a;
  }
  * { margin: 0; padding: 0; box-sizing: border-box; }
  html, body { width: 900px; height: 1200px; overflow: hidden; background: var(--paper); }
  .flyer {
    position: relative; width: 900px; height: 1200px; overflow: hidden;
    font-family: 'Delius', sans-serif; color: var(--ink);
  }
  .beach-scene {
    position: absolute; inset: 0;
    background: linear-gradient(180deg,
      var(--paper) 0%, var(--paper) 36%,
      var(--sky-mist) 48%,
      var(--hill-blue) 60%,
      var(--sea-grey) 68%,
      var(--sand-gold) 71%,
      var(--wet-sand) 74%,
      #dfe3e6 86%, #c9ced3 100%);
  }
  .headline { position: absolute; top: 44px; left: 0; right: 0; }
  .headline__name {
    font-family: 'Courgette', cursive; font-weight: 400; font-size: 70px; line-height: 1;
    text-align: center;
  }
  .headline__tagline {
    font-size: 30px; margin-top: 8px; text-align: right; padding-right: 90px;
  }
  .intro {
    position: absolute; top: 208px; left: 86px; right: 80px;
    font-size: 15.5px; line-height: 1.45;
  }
  .benefits-lead { position: absolute; top: 302px; left: 86px; font-size: 15px; }
  .benefits {
    position: absolute; top: 340px; left: 100px; right: 90px; list-style: none;
    font-size: 15px; line-height: 1.35;
  }
  .benefits li { position: relative; padding-left: 22px; margin-bottom: 10px; }
  .benefits li::before { content: "-"; position: absolute; left: 0; }
  .cta {
    position: absolute; top: 702px; left: 0; right: 0; text-align: center;
    font-size: 20px; line-height: 1.35;
  }
  .presenter {
    position: absolute; left: 88px; top: 998px; width: 744px; height: 172px;
    background: var(--card-veil); padding: 10px 18px 10px 134px;
  }
  .presenter__photo {
    position: absolute; left: 14px; top: 34px; width: 100px; height: 100px;
    background: linear-gradient(160deg, #c8cfc4, var(--photo-tone));
  }
  .presenter__title { font-family: 'Dancing Script', cursive; font-size: 24px; line-height: 1.2; margin-bottom: 4px; }
  .presenter p { font-size: 12.5px; line-height: 1.38; margin-bottom: 8px; }
</style>
</head>
<body>
<main class="flyer">
  <div class="beach-scene" role="img" aria-label="Misty beach at low tide with distant hills and a couple walking hand in hand along the wet sand"></div>

  <header class="headline">
    <h1 class="headline__name">Lantern Bridge Days</h1>
    <p class="headline__tagline">and bring out the best in each other</p>
  </header>

  <p class="intro">Some couples spend up big on their wedding day but fail to invest in their marriage or relationship, but relationships take much more than love to be successful. This innovative one-day seminar helps couples to breathe new life into their relationship.</p>

  <p class="benefits-lead">What you will gain from Rowan's seminar:</p>
  <ul class="benefits">
    <li>How to turn an argument into a moment of closeness – Easier than you think!</li>
    <li>Know what stress is doing to your relating and the two skillsets will make a big difference to each other's stress-load.</li>
    <li>The role of pleasure in an emotionally-committed relationship and that's more than sex!</li>
    <li>Identify the traps of committed relationships – and why being in a relationship doesn't have to be a struggle.</li>
    <li>Learn how it's not you or your partner's fault – Identify the missing ingredients in relationship and what you can do to get these back.</li>
    <li>What the research says about the ingredients of great sex</li>
    <li>What to do about the three drains on your relationship: boredom, having nothing to say and those same-old arguments.</li>
    <li>You will also practice using Rowan's negotiation tool that he developed for couples as well. Rowan's seminars are fun, informative and practical.</li>
  </ul>

  <p class="cta">Take your relationship to the next level and book your seat now:<br>http://www.rowanashbycoaching.com.au/couples.html</p>

  <aside class="presenter">
    <div class="presenter__photo" role="img" aria-label="Portrait of the presenter"></div>
    <h2 class="presenter__title">About the presenter:</h2>
    <p>Rowan Ashby is a highly skilled couples therapist and educator, who is known for his innovative and creative approaches in his work. He has appeared on Harbourline TV's The Early Edition and Northgate Network's Night Desk as well as being interviewed on radio and in print.</p>
    <p>Rowan's seminars run along brain-based education principles that he learnt from Dr Alan Wexford's training in the USA, so that you will remember your new learning and integrate it into your life.</p>
  </aside>
</main>
</body>
</html>
```